Business Card Design

We are a state licensed general contractor on the south east coast of Florida. We are a remodeling and home repairs business that have been in business for 14 years. Since we are located on the coast and our business name is Ridgeway Builders of Lower Meadow, Inc, we would like a "Ridgeway" themed design that would appeal to more affluent customers. I would like to see light blue colors with waves incorporated into the design. I would also like the design to communicate a modern, confident, responsible company character.

Industry/Entity Type

Contractor

Contact Information for Business Card

Tim Harlow 555-276-3148

```html
<!DOCTYPE html>
<html lang="en">
<head>
<meta charset="utf-8">
<title>Ridgeway Builders – Business Card</title>
<link href="https://fonts.googleapis.com/css2?family=Michroma&family=Montserrat:wght@400;500;600;700&display=swap" rel="stylesheet">
<style>
  :root {
    --bg: #e9ebee;
    --card: #ffffff;
    --navy: #0d3a78;
    --sky: #3d9fdc;
    --ink: #2f3440;
    --rule: #b9bec7;
  }
  * { box-sizing: border-box; margin: 0; padding: 0; }
  html, body { width: 1200px; height: 800px; overflow: hidden; }
  body {
    background: var(--bg);
    font-family: "Montserrat", sans-serif;
    color: var(--ink);
    position: relative;
  }
  .card {
    position: absolute;
    top: 120px;
    width: 340px;
    height: 560px;
    background: linear-gradient(160deg, #ffffff 0%, #f3f4f6 100%);
    box-shadow: 0 10px 28px rgba(0,0,0,0.16);
    overflow: hidden;
  }
  .card--front { left: 220px; }
  .card--back  { left: 640px; }

  .corner-fold { position: absolute; top: 0; left: 0; width: 110px; height: 130px; }

  .brand { text-align: center; }
  .brand__name {
    font-family: "Montserrat", sans-serif;
    font-weight: 600;
    color: var(--navy);
    letter-spacing: 0.5px;
    display: inline-flex;
    align-items: center;
    gap: 10px;
  }
  .brand__dot {
    width: 14px; height: 14px; border-radius: 50%;
    background: var(--sky);
    flex: none;
  }

  .card--front .brand { position: absolute; top: 150px; left: 0; right: 0; }
  .card--front .brand__name { font-size: 26px; }

  .person { position: absolute; top: 220px; left: 60px; }
  .person__name {
    font-family: "Michroma", sans-serif;
    font-size: 17px;
    color: var(--navy);
    letter-spacing: 1px;
  }
  .person__role { font-size: 14px; font-weight: 500; margin-top: 6px; color: var(--ink); }

  .contacts { position: absolute; top: 300px; left: 60px; right: 45px; list-style: none; }
  .contact {
    display: flex; align-items: center; gap: 12px;
    padding: 10px 0;
    border-bottom: 1px solid var(--rule);
    font-size: 11.5px;
    line-height: 1.4;
  }
  .contact__icon { width: 16px; height: 16px; flex: none; fill: var(--navy); }

  .card--back .brand { position: absolute; top: 255px; left: 0; right: 0; }
  .card--back .brand__name { font-size: 30px; }
  .website {
    position: absolute; bottom: 70px; left: 0; right: 0;
    text-align: center;
    font-size: 13px; font-weight: 600;
    letter-spacing: 2.5px;
    color: var(--navy);
  }
</style>
</head>
<body>

  <section class="card card--front" aria-label="Business card front">
    <svg class="corner-fold" viewBox="0 0 110 130" aria-hidden="true">
      <polygon points="0,0 70,0 0,130" fill="var(--navy)"/>
      <polygon points="30,0 100,0 62,62 18,118" fill="var(--sky)"/>
    </svg>

    <div class="brand">
      <span class="brand__name"><span class="brand__dot"></span>Ridgeway Builders</span>
    </div>

    <div class="person">
      <h1 class="person__name">TIM HARLOW</h1>
      <p class="person__role">Managing Director</p>
    </div>

    <ul class="contacts">
      <li class="contact">
        <svg class="contact__icon" viewBox="0 0 24 24" aria-hidden="true"><path d="M6.6 10.8a15 15 0 0 0 6.6 6.6l2.2-2.2c.3-.3.7-.4 1-.2 1.1.4 2.3.6 3.6.6.6 0 1 .4 1 1V20c0 .6-.4 1-1 1A17 17 0 0 1 3 4c0-.6.4-1 1-1h3.5c.6 0 1 .4 1 1 0 1.3.2 2.5.6 3.6.1.3 0 .7-.2 1z"/></svg>
        <span>555-276-3148</span>
      </li>
      <li class="contact">
        <svg class="contact__icon" viewBox="0 0 24 24" aria-hidden="true"><path d="M3 5h18v14H3z M3 5l9 7 9-7" fill="none" stroke="var(--navy)" stroke-width="2"/></svg>
        <span>tim@ridgewaybuild.com</span>
      </li>
      <li class="contact">
        <svg class="contact__icon" viewBox="0 0 24 24" aria-hidden="true"><circle cx="12" cy="12" r="9" fill="none" stroke="var(--navy)" stroke-width="2"/><path d="M3 12h18M12 3c3 3 3 15 0 18M12 3c-3 3-3 15 0 18" fill="none" stroke="var(--navy)" stroke-width="1.6"/></svg>
        <span>www.ridgewaybuild.com</span>
      </li>
      <li class="contact">
        <svg class="contact__icon" viewBox="0 0 24 24" aria-hidden="true"><path d="M12 2a7 7 0 0 0-7 7c0 5 7 13 7 13s7-8 7-13a7 7 0 0 0-7-7zm0 9.5a2.5 2.5 0 1 1 0-5 2.5 2.5 0 0 1 0 5z"/></svg>
        <span>48 Harbor Lane, Lower Meadow<br>3307</span>
      </li>
    </ul>
  </section>

  <section class="card card--back" aria-label="Business card back">
    <div class="brand">
      <span class="brand__name"><span class="brand__dot"></span>Ridgeway Builders</span>
    </div>
    <p class="website">www.ridgewaybuild.com</p>
  </section>

</body>
</html>
```